Letterhead designs for Property Management firm

Would like to see some different letterhead/envelope designs We are a residential property management company. We would like to see designs that utilize blue/grays/black

```html
<!DOCTYPE html>
<html lang="en">
<head>
<meta charset="utf-8">
<title>Ridgeway Property Management – Stationery</title>
<link rel="stylesheet" href="https://fonts.googleapis.com/css2?family=Open+Sans:wght@400;800&display=swap">
<style>
  :root {
    --canvas: #e4e6e9;
    --paper: #ffffff;
    --rule: #6b6e72;
    --ink: #3a3c40;
    --brand-blue: #1f4fa8;
    --shadow: rgba(20, 24, 30, 0.18);
  }
  * { box-sizing: border-box; margin: 0; padding: 0; }
  html, body {
    width: 1200px; height: 1200px; overflow: hidden;
    background: var(--canvas);
    font-family: "Open Sans", Arial, sans-serif;
    color: var(--ink);
  }
  .sheet {
    position: absolute;
    background: var(--paper);
    box-shadow: 0 6px 24px var(--shadow);
  }
  .sheet svg.frame { position: absolute; inset: 0; }
  .frame line { stroke: var(--rule); stroke-width: 1.2; }

  .brand {
    position: absolute;
    display: flex; align-items: center; gap: 10px;
    color: var(--brand-blue);
    font-weight: 800;
    text-transform: uppercase;
    line-height: 1.1;
    white-space: nowrap;
  }
  .brand-mark { background: var(--brand-blue); flex: none; }

  /* Letterhead */
  .letterhead { left: 60px; top: 212px; width: 600px; height: 776px; }
  .letterhead .brand { left: 0; right: 0; top: 18px; justify-content: center; font-size: 17px; text-align: left; }
  .letterhead .brand-mark { width: 22px; height: 22px; }
  .letterhead .footer {
    position: absolute; left: 70px; right: 50px; bottom: 16px;
    font-size: 11px; letter-spacing: 0.2px; text-align: center;
  }
  .letterhead .footer p + p { margin-top: 2px; }

  /* Envelope */
  .envelope { left: 700px; top: 500px; width: 460px; height: 200px; }
  .envelope .brand { left: 22px; top: 16px; font-size: 13px; gap: 8px; }
  .envelope .brand-mark { width: 16px; height: 16px; }
  .envelope .return-address {
    position: absolute; left: 28px; bottom: 14px;
    font-size: 9px; letter-spacing: 0.2px; white-space: nowrap;
  }
</style>
</head>
<body>

<section class="sheet letterhead" aria-label="Letterhead">
  <svg class="frame" width="600" height="776" aria-hidden="true">
    <line x1="24" y1="24" x2="160" y2="24"/>
    <line x1="440" y1="24" x2="576" y2="24"/>
    <line x1="24" y1="24" x2="24" y2="752"/>
    <line x1="576" y1="24" x2="576" y2="752"/>
    <line x1="24" y1="752" x2="62" y2="752"/>
    <line x1="556" y1="752" x2="576" y2="752"/>
  </svg>
  <div class="brand">
    <span class="brand-mark"></span>
    <span>Ridgeway<br>Property Management</span>
  </div>
  <div class="footer">
    <p>Dummy city, Dummy Country Land Dummy</p>
    <p>1-555-010-2040 | info@ridgewaypm.com | www.ridgewaypm.com</p>
  </div>
</section>

<section class="sheet envelope" aria-label="Envelope">
  <svg class="frame" width="460" height="200" aria-hidden="true">
    <line x1="250" y1="20" x2="440" y2="20"/>
    <line x1="20" y1="70" x2="20" y2="180"/>
    <line x1="440" y1="20" x2="440" y2="180"/>
    <line x1="20" y1="180" x2="24" y2="180"/>
    <line x1="240" y1="180" x2="440" y2="180"/>
  </svg>
  <div class="brand">
    <span class="brand-mark"></span>
    <span>Ridgeway<br>Property Management</span>
  </div>
  <p class="return-address">Dummy city, Dummy Country Land Dummy</p>
</section>

</body>
</html>
```